business card for a shoe shop

we would like a business card for a family owned shoe shop.
With this information included.
Darnell's Shoe Store
Family owned since 1947

then on other side
Darnell's Shoe Store
Footwear fitting specialist
Phone: 9187 2630
218 Quarry St, Fernleigh Downs 3187
(cnr. Hartwick Rd and Quarry St)
darnellshoes218@examplemail.com
if could incorporate the purple color on card i have attached.

```html
<!DOCTYPE html>
<html lang="en">
<head>
<meta charset="utf-8">
<title>Darnell's Shoe Store – Business Card</title>
<link href="https://fonts.googleapis.com/css2?family=Libre+Baskerville&family=Quicksand:wght@500;600&display=swap" rel="stylesheet">
<style>
  :root {
    --backdrop: #e4d9ec;
    --card: #f6f5f7;
    --purple: #6c4fa0;
    --lavender-soft: #ece6f3;
    --ink-muted: #7a5fae;
  }
  * { margin: 0; padding: 0; box-sizing: border-box; }
  html, body {
    width: 1200px; height: 1200px; overflow: hidden;
    background: var(--backdrop);
  }
  .canvas {
    position: relative; width: 1200px; height: 1200px;
    display: flex; flex-direction: column; align-items: center; justify-content: center; gap: 60px;
  }
  .card {
    position: relative; width: 720px; height: 410px;
    border-radius: 18px; overflow: hidden;
    background: var(--card);
    box-shadow: 0 14px 30px rgba(90, 60, 120, 0.18);
  }
  .brand-name {
    font-family: "Libre Baskerville", serif; font-weight: 400;
    color: var(--purple); font-size: 29px; letter-spacing: 4.5px;
    text-transform: uppercase; white-space: nowrap; text-align: center;
  }
  /* front */
  .card-front .wave-field {
    position: absolute; inset: 0;
    background: linear-gradient(160deg, #f4f0f8 0%, var(--lavender-soft) 50%, #f2edf7 100%);
  }
  .front-content {
    position: absolute; inset: 0;
    display: flex; flex-direction: column; align-items: center; justify-content: center;
  }
  .tagline {
    font-family: "Quicksand", sans-serif; font-weight: 600;
    color: var(--purple); font-size: 15px; letter-spacing: 2.5px;
    margin-top: 16px;
  }
  /* back */
  .card-back .side-band {
    position: absolute; left: 0; top: 0; bottom: 0; width: 87px;
    background: linear-gradient(180deg, #7152a6, #6a4d9d);
  }
  .back-content { position: absolute; left: 87px; right: 0; top: 0; bottom: 0; padding: 68px 0 0 50px; }
  .back-header { width: 500px; text-align: center; }
  .back-header .brand-name { font-size: 31px; }
  .specialty {
    font-family: "Libre Baskerville", serif;
    color: var(--purple); font-size: 15px; letter-spacing: 4px;
    text-transform: uppercase; margin-top: 12px; white-space: nowrap;
  }
  .contact-list { list-style: none; margin-top: 50px; }
  .contact-item { display: flex; align-items: flex-start; gap: 20px; margin-bottom: 18px; }
  .contact-icon { flex: none; width: 38px; height: 38px; }
  .contact-text {
    font-family: "Quicksand", sans-serif; font-weight: 500;
    color: var(--ink-muted); font-size: 19px; line-height: 27px; padding-top: 5px;
  }
  .contact-phone .contact-text { font-size: 25px; padding-top: 3px; }
</style>
</head>
<body>
<main class="canvas">

  <section class="card card-front">
    <div class="wave-field" role="img" aria-label="Fine lavender wave line pattern covering the card"></div>
    <div class="front-content">
      <h1 class="brand-name">Darnell’s Shoe Store</h1>
      <p class="tagline">Family Owned Since 1947</p>
    </div>
  </section>

  <section class="card card-back">
    <div class="side-band" role="img" aria-label="Purple band with white wave line pattern"></div>
    <div class="back-content">
      <header class="back-header">
        <h2 class="brand-name">Darnell's Shoe Store</h2>
        <p class="specialty">Footwear Fitting Specialist</p>
      </header>
      <ul class="contact-list">
        <li class="contact-item contact-phone">
          <svg class="contact-icon" viewBox="0 0 38 38" aria-hidden="true">
            <circle cx="19" cy="19" r="19" fill="#6c4fa0"/>
            <path d="M13 11c1-.8 2-.6 2.6.3l1.8 2.8c.5.8.3 1.6-.4 2.2l-1.2 1c.9 2 2.4 3.5 4.4 4.4l1-1.2c.6-.7 1.4-.9 2.2-.4l2.8 1.8c.9.6 1.1 1.6.3 2.6l-1.2 1.4c-1 1-3 1.2-5.4 0-3.3-1.6-6-4.3-7.6-7.6-1.2-2.4-1-4.4 0-5.4z" fill="#fff"/>
            <path d="M21 11.5a6 6 0 0 1 5.5 5.5M21 14.5a3 3 0 0 1 2.5 2.5" stroke="#fff" stroke-width="1.4" fill="none" stroke-linecap="round"/>
          </svg>
          <span class="contact-text">9187 2630</span>
        </li>
        <li class="contact-item">
          <svg class="contact-icon" viewBox="0 0 38 38" aria-hidden="true">
            <circle cx="19" cy="19" r="19" fill="#6c4fa0"/>
            <path d="M19 9a6.5 6.5 0 0 0-6.5 6.5c0 4.8 6.5 12.5 6.5 12.5s6.5-7.7 6.5-12.5A6.5 6.5 0 0 0 19 9z" fill="#fff"/>
            <circle cx="19" cy="15.5" r="2.4" fill="#6c4fa0"/>
          </svg>
          <span class="contact-text">218 Quarry St, Fernleigh Downs 3187<br>(cnr. Hartwick Rd and Quarry St)</span>
        </li>
        <li class="contact-item">
          <svg class="contact-icon" viewBox="0 0 38 38" aria-hidden="true">
            <circle cx="19" cy="19" r="19" fill="#6c4fa0"/>
            <rect x="10.5" y="13" width="17" height="12" rx="1.5" fill="#fff"/>
            <path d="M11 13.8l8 6 8-6M11 24.4l6-5M27 24.4l-6-5" stroke="#6c4fa0" stroke-width="1.3" fill="none"/>
          </svg>
          <span class="contact-text">darnellshoes218@examplemail.com</span>
        </li>
      </ul>
    </div>
  </section>

</main>
</body>
</html>
```